Designing a label for Convertible Hood Cleaner (also 6 more labels to design in the future)

We have a range of cleaning products which we need to update label designs

This competition is just for one design but once a winner has been selected we have a lot more work for you including 6 more labels and a new logo.

Please see files for content. This product is very popular but the label is outdated.

Size of label - 110mm x 75mm
This will be a sticky label to be added to a sachet (white ziplock pouch)

Colors

Designer to choose colors to be used in the design.

```html
<!DOCTYPE html>
<html lang="en">
<head>
<meta charset="utf-8">
<title>Heavy Duty Convertible Soft Top Cleaner – Label</title>
<link rel="stylesheet" href="https://fonts.googleapis.com/css2?family=Archivo+Black&display=swap">
<style>
  :root {
    --sky-top: #a9bfdc;
    --sky-mid: #dbe6f2;
    --sky-light: #f3f7fb;
    --brand-red: #e8202a;
    --label-grey: #e9eaec;
    --tagline-blue: #3f86c8;
    --ink: #111111;
    --white: #ffffff;
  }
  * { margin: 0; padding: 0; box-sizing: border-box; }
  html, body { width: 892px; height: 1200px; overflow: hidden; background: var(--white); }
  .label {
    position: relative;
    width: 892px;
    height: 1200px;
    overflow: hidden;
    font-family: "Archivo Black", "Arial Black", sans-serif;
    background: radial-gradient(ellipse at 50% 45%, var(--sky-light) 0%, var(--sky-mid) 45%, var(--sky-top) 100%);
  }
  .brand {
    position: absolute;
    top: 118px; left: 0; width: 100%;
    display: flex; justify-content: center; align-items: center; gap: 14px;
  }
  .brand-mark { width: 30px; height: 30px; background: var(--brand-red); }
  .brand-name { color: var(--brand-red); font-size: 50px; line-height: 64px; letter-spacing: 1px; }
  .headline {
    position: absolute;
    top: 250px; left: 0; width: 100%;
    text-align: center;
    color: var(--brand-red);
    font-size: 70px;
    line-height: 76px;
    -webkit-text-stroke: 6px var(--white);
    paint-order: stroke fill;
  }
  .product-photo {
    position: absolute;
    left: 116px; top: 512px; width: 752px; height: 430px;
    background: radial-gradient(ellipse at 55% 55%, #f4f4f4 0%, #d9dcdf 45%, #8e9298 80%, #6c7076 100%);
    clip-path: polygon(18% 0%, 80% 0%, 100% 35%, 100% 100%, 50% 100%, 48% 83%, 0% 83%, 0% 20%);
  }
  .footer-bands { position: absolute; left: 0; top: 962px; width: 892px; height: 238px; }
  .tagline {
    position: absolute;
    left: 52px; top: 884px;
    color: var(--tagline-blue);
    font-size: 35px;
    line-height: 39px;
  }
  .cleans-list {
    position: absolute;
    left: 52px; top: 1030px;
    color: var(--white);
    font-size: 33px;
    line-height: 42px;
  }
  .yield {
    position: absolute;
    left: 594px; top: 1062px;
    display: flex; align-items: center;
    color: var(--ink);
    -webkit-text-stroke: 5px var(--white);
    paint-order: stroke fill;
  }
  .yield-number { font-size: 120px; line-height: 110px; }
  .yield-words { font-size: 40px; line-height: 42px; margin-left: 4px; }
</style>
</head>
<body>
  <main class="label">
    <div class="brand">
      <span class="brand-mark"></span>
      <span class="brand-name">PADDOCK N KERB</span>
    </div>

    <h1 class="headline">HEAVY DUTY<br>CONVERTIBLE SOFT<br>TOP CLEANER</h1>

    <div class="product-photo" role="img" aria-label="Photo of a white convertible car with a black fabric soft top, seen from the rear three-quarter view"></div>

    <svg class="footer-bands" viewBox="0 0 892 238" aria-hidden="true">
      <rect x="0" y="0" width="892" height="238" fill="var(--label-grey)"/>
      <path d="M0 60 H440 C500 60 520 80 545 110 C570 140 590 153 640 153 H892 V238 H0 Z" fill="var(--brand-red)"/>
    </svg>

    <p class="tagline">Quick &amp; Easy<br>To Use For<br>Professional Results</p>

    <p class="cleans-list">cleans: dirt-grime<br>stains - mould<br>and mildew</p>

    <div class="yield">
      <span class="yield-number">2</span>
      <span class="yield-words">Makes<br>Liters</span>
    </div>
  </main>
</body>
</html>
```